Your CBD Harbor Nook Print Ad - Magazine/Coupon Booklet

Create a 4-Color, Full Page Print Ad that promotes our store, Your CBD Harbor Nook, and that includes a coupon offer positioned the bottom of the page that takes up about 25% of the space (offer details below). <br/><br/>About Your CBD Harbor Nook: We are family-owned, CBD retail and online store, committed to educating consumers about the benefits and science behind CBD, helping customers discern fact from fiction and hype from reality so they can learn to evaluate and discern what products would work best for themselves, their families…and their pets. <br/><br/>We carry a variety of CBD brands:<br/> - Wren CBD<br/> - Tulavista<br/> - CBD Falcon<br/> - Brindlemoor Essentials<br/> - Quillfield Remedies<br/> - Amber Fern<br/> - CBDPup Wellness<br/> - Zorvo Morsels<br/>- Finding Warmer Mornings<br/><br/>Within these brands, we carry the following types of CBD-infused products: <br/> - Oil Tinctures, <br/> - Topicals, including lotions, creams, balms, body oils and bath bombs<br/> - Edibles, including gummies, taffy, coffee and beverage enhancers<br/> - Pet Products, including chew treats, balms and tinctures<br/><br/>The ad should include our logo and reflect our store's brand image. I've included photos of the inside of the store to give you the look and feel of our store. <br/><br/>Coupon Offer: <br/>The bottom part of the ad needs to include a Offer portion that is easily identifiable as a coupon (ie, area bordered at top with horizontal dash lines....see attached example)<br/><br/>Offer: <br/>Join the Nook Rewards Circle and receive 15% off your first purchase and 10% - or more - off ALL future purchases!<br/>Join today in person, or OR online at www.club.yourcbdnookplace.com (https://paytilly.example/loyalty/Q3RTXNHJ92LFA)<br/><br/><br/>SIZE/SPECS:<br/>FULL PAGE, 4C<br/>Ad Area: 4.194" x 3.924" <br/>Offer Portion: 4.194” x 1.271"
Updates

UPDATE Information about the Ad Size and Specifications and File Format (from the publisher) FULL PAGE, 4C Ad: Ad Area: 4.194" x 3.924" Offer (coupon) Portion: (this area is located on the BOTTOM of the ad) 4.194” x 1.271" NOTE: The offer portion of the coupon must have a white background and we ask that graphics be limited to your company logo(s). PREFERRED FILE FORMAT: Hi-res PDF files with fonts embedded

Must be a vertical - not horizontal - ad.

Target Market(s)

A25-64, area residents of zip code 30022. Demographics are upscale, married, homeowners

Industry/Entity Type

Supplement

Font styles to use
Serif
Sans Serif

Colors
00a990
a64599

Requirements
Must have
• Leaf- Leaf- Huzzah!!! Calm Has Arrived
• Our doors have opened right down the street on Pendergast Mill Road
• We are not a franchise, but a family-owned business who have personally benefited from the wonders of CBD and are no introducing these benefits to others in our community, all from our little store on Pendergast Mill Road!
• Our Commitment to Quality Offerings
• We carry only a select few brands that meet – or exceed – the highest standards of quality, integrity, and efficacy. No unsubstantiated claims, no false labeling, each product is accompanied by their Certificate of Authority (COA) to ensure consistency and quality. In addition, our products are all hemp-sourced from family owned farms, are organic (when possible), and carry a 30 day money-back guarantee.
• Our Commitment to Educated Consumers
• By educating, sharing knowledge, and bringing expertise and personal testimonials to our customers, we're looking to create a community of well-informed consumers who confidently make well-informed decisions about the products they’ve chosen.
• Helping customers make the best decisions for the wellness of themselves, their families...including their beloved fur babies…is our nirvana!
• [OFFER PORTION]
• JOIN THE NOOK REWARDS CIRCLE TODAY!
• Sign up for our Nook Rewards Circle for free and receive 15% off your first purchase in store or online. Nook Circle members then receive an additional 10% off all future CBD purchases!
• Visit us in the store or online at: www.club.yourcbdnookplace.com to sign up!
• Your CBD Harbor Nook
• 2846 Pendergast Mill Road, Suite 412
• Roswell, GA 30076
• (next door to Brewlark, two doors down from TorvinFunhouse)
• Photo of inside of store
• Logo
• (855) 731-4092
• NOTE: The offer portion of the coupon must have a white background and we ask that graphics be limited to our company logo(s).

```html
<!DOCTYPE html>
<html lang="en">
<head>
<meta charset="utf-8">
<title>Your CBD Harbor Nook – Print Ad</title>
<link href="https://fonts.googleapis.com/css2?family=Lobster&family=Source+Sans+3:wght@400;600;700;900&display=swap" rel="stylesheet">
<style>
  :root{
    --purple:#4a1d6a;
    --purple-deep:#3b1556;
    --green:#6cab3c;
    --green-dark:#4f8a2a;
    --white:#ffffff;
    --page:#ececec;
    --grey-text:#6b6b6b;
    --dash:#9a8aa8;
  }
  *{margin:0;padding:0;box-sizing:border-box}
  html,body{width:1129px;height:1200px;overflow:hidden;background:var(--page)}
  body{font-family:"Source Sans 3",Arial,sans-serif;position:relative}
  .ad{position:absolute;left:99px;top:23px;width:930px;height:1154px;background:var(--white);overflow:hidden;box-shadow:0 4px 14px rgba(0,0,0,.18)}
  .ad-art{position:absolute;left:0;top:0;width:930px;height:870px}
  .brand{position:absolute;left:34px;top:60px;display:flex;align-items:center;gap:12px}
  .brand-dot{width:38px;height:38px;border-radius:50%;background:var(--green)}
  .brand-name{font-weight:900;font-size:31px;line-height:1.05;color:var(--purple);width:190px}
  .intro{position:absolute;left:28px;top:530px;width:880px;color:var(--white)}
  .headline{font-family:"Lobster",cursive;font-size:29px;color:var(--green);font-weight:400;margin-bottom:16px}
  .intro p{font-size:18px;line-height:1.42;margin-bottom:10px}
  .promises{position:absolute;left:70px;top:790px;width:820px;display:grid;grid-template-columns:440px 380px;row-gap:12px;list-style:none;color:var(--white);font-size:22px;font-weight:600}
  .promises li{display:flex;align-items:center;gap:12px}
  .promises svg{width:26px;height:26px;flex:none}
  .offer{position:absolute;left:0;top:870px;width:930px;height:229px;background:var(--white);text-align:center;border-top:3px dashed var(--dash)}
  .offer-title{margin-top:18px;font-weight:900;font-size:34px;color:var(--purple);letter-spacing:.3px}
  .offer-text{margin:6px auto 0;width:850px;font-weight:700;font-size:18px;line-height:1.35;color:var(--green-dark)}
  .offer-pill{display:inline-flex;align-items:center;gap:8px;margin-top:13px;padding:9px 34px;border-radius:24px;background:var(--purple);color:var(--white);font-size:17px}
  .offer-pill b{font-weight:700}
  .offer-pill svg{width:18px;height:18px}
  .offer-link{margin-top:8px;font-size:17px;font-weight:600;color:var(--grey-text)}
  .contact{position:absolute;left:0;top:1099px;width:930px;height:55px;background:var(--green);color:var(--white);display:flex;align-items:center;justify-content:space-between;padding:0 30px 0 22px;font-size:15px;font-weight:600}
  .contact-item{display:flex;align-items:center;gap:8px}
  .contact-item svg{width:20px;height:20px;flex:none}
  .contact-address small{display:block;font-size:11px;font-weight:600;line-height:1.1}
</style>
</head>
<body>
<main class="ad">
  <svg class="ad-art" viewBox="0 0 930 870" width="930" height="870">
    <defs>
      <linearGradient id="storeWall" x1="0" y1="0" x2="0" y2="1">
        <stop offset="0" stop-color="#a0634c"/>
        <stop offset=".35" stop-color="#8c5443"/>
        <stop offset=".62" stop-color="#5a4034"/>
        <stop offset="1" stop-color="#3e3a2e"/>
      </linearGradient>
      <radialGradient id="storePlants" cx=".88" cy=".55" r=".45">
        <stop offset="0" stop-color="#4e7a34" stop-opacity=".95"/>
        <stop offset=".6" stop-color="#3f5e2c" stop-opacity=".55"/>
        <stop offset="1" stop-color="#3f5e2c" stop-opacity="0"/>
      </radialGradient>
      <radialGradient id="storeLight" cx=".5" cy=".35" r=".4">
        <stop offset="0" stop-color="#d9c2a6" stop-opacity=".35"/>
        <stop offset="1" stop-color="#d9c2a6" stop-opacity="0"/>
      </radialGradient>
      <linearGradient id="productTones" x1="0" y1="0" x2="1" y2="1">
        <stop offset="0" stop-color="#c9d6e0"/>
        <stop offset="1" stop-color="#8c6b7a"/>
      </linearGradient>
      <linearGradient id="packTones" x1="0" y1="0" x2="1" y2="1">
        <stop offset="0" stop-color="#b98b55"/>
        <stop offset="1" stop-color="#5a4a3a"/>
      </linearGradient>
    </defs>
    <g role="img" aria-label="Photo of the store interior with brick wall, product shelves and plants">
      <rect x="0" y="0" width="930" height="600" fill="url(#storeWall)"/>
      <rect x="0" y="0" width="930" height="600" fill="url(#storeLight)"/>
      <rect x="0" y="0" width="930" height="600" fill="url(#storePlants)"/>
    </g>
    <path class="logo-curve" d="M0,0 H400 C360,40 330,130 250,210 C180,270 80,290 0,300 Z" fill="var(--white)"/>
    <path class="logo-curve-edge" d="M400,0 C360,40 330,130 250,210 C180,270 80,290 0,300" fill="none" stroke="var(--green)" stroke-width="4"/>
    <path class="purple-band" d="M0,395 C260,470 520,520 930,500 L930,870 L0,870 Z" fill="var(--purple)"/>
    <path class="band-edge" d="M0,395 C260,470 520,520 930,500" fill="none" stroke="var(--green)" stroke-width="5"/>
    <circle cx="618" cy="448" r="88" fill="var(--white)" opacity=".85"/>
    <circle cx="618" cy="448" r="78" fill="url(#productTones)" role="img" aria-label="Photo of CBD topical products"/>
    <circle cx="795" cy="424" r="108" fill="var(--white)" opacity=".85"/>
    <circle cx="795" cy="424" r="98" fill="url(#packTones)" role="img" aria-label="Photo of CBD edibles and pet product packages"/>
  </svg>

  <div class="brand">
    <span class="brand-dot"></span>
    <span class="brand-name">Your CBD Harbor Nook</span>
  </div>

  <section class="intro">
    <h1 class="headline">Leaf- Leaf- Huzzah!!! Calm Has Arrived</h1>
    <p>Our doors have opened right down the street on Pendergast Mill Road</p>
    <p>We are not a franchise, but a family-owned business who have personally benefited from the wonders of CBD and are no introducing these benefits to others in our community, all from our little store on Pendergast Mill Road! Our Commitment to Quality Offerings .</p>
    <p>We carry only a select few brands that meet – or exceed – the highest standards of quality, integrity, and efficacy.</p>
  </section>

  <ul class="promises">
    <li><svg viewBox="0 0 26 26"><rect x="1" y="5" width="20" height="20" fill="var(--white)"/><path d="M5 14 l5 5 L24 3" fill="none" stroke="var(--green)" stroke-width="4"/></svg>No unsubstantiated claims</li>
    <li><svg viewBox="0 0 26 26"><rect x="1" y="5" width="20" height="20" fill="var(--white)"/><path d="M5 14 l5 5 L24 3" fill="none" stroke="var(--green)" stroke-width="4"/></svg>Our products are organic</li>
    <li><svg viewBox="0 0 26 26"><rect x="1" y="5" width="20" height="20" fill="var(--white)"/><path d="M5 14 l5 5 L24 3" fill="none" stroke="var(--green)" stroke-width="4"/></svg>No false labeling (COA)</li>
    <li><svg viewBox="0 0 26 26"><rect x="1" y="5" width="20" height="20" fill="var(--white)"/><path d="M5 14 l5 5 L24 3" fill="none" stroke="var(--green)" stroke-width="4"/></svg>30 day money-back guarantee</li>
  </ul>

  <section class="offer">
    <h2 class="offer-title">JOIN THE NOOK REWARDS CIRCLE TODAY!</h2>
    <p class="offer-text">Sign up for our Nook Rewards Circle for free and receive 15% off your first purchase in store or online. Nook Circle members then receive an additional 10% off all future CBD purchases!</p>
    <div class="offer-pill">Visit us in the store or online at:
      <svg viewBox="0 0 18 18"><circle cx="9" cy="9" r="7.5" fill="none" stroke="var(--white)" stroke-width="1.6"/><path d="M1.5 9 H16.5 M9 1.5 C5 6 5 12 9 16.5 M9 1.5 C13 6 13 12 9 16.5" fill="none" stroke="var(--white)" stroke-width="1.3"/></svg>
      <b>www.club.yourcbdnookplace.com</b> to sign up!</div>
    <p class="offer-link">https://paytilly.example/loyalty/Q3RTXNHJ92LFA</p>
  </section>

  <footer class="contact">
    <div class="contact-item contact-address">
      <svg viewBox="0 0 20 20"><circle cx="10" cy="10" r="10" fill="var(--white)"/><path d="M10 4 a4 4 0 0 1 4 4 c0 3 -4 8 -4 8 s-4 -5 -4 -8 a4 4 0 0 1 4 -4z" fill="var(--green)"/></svg>
      <span>2846 Pendergast Mill Road, Suite 412 Roswell, GA 30076<small>(right next to Brewlark, two doors down from TorvinFunhouse)</small></span>
    </div>
    <div class="contact-item">
      <svg viewBox="0 0 20 20"><circle cx="10" cy="10" r="10" fill="var(--white)"/><path d="M6.5 5 l2 0 1 3 -1.5 1 a7 7 0 0 0 3 3 l1 -1.5 3 1 0 2 a1.5 1.5 0 0 1 -1.5 1.5 A9 9 0 0 1 5 6.5 A1.5 1.5 0 0 1 6.5 5z" fill="var(--green)"/></svg>
      <span>(855) 731-4092</span>
    </div>
    <div class="contact-item">
      <svg viewBox="0 0 20 20"><circle cx="10" cy="10" r="10" fill="var(--white)"/><circle cx="10" cy="10" r="5.5" fill="none" stroke="var(--green)" stroke-width="1.4"/><path d="M4.5 10 H15.5 M10 4.5 C7 8 7 12 10 15.5 M10 4.5 C13 8 13 12 10 15.5" fill="none" stroke="var(--green)" stroke-width="1.2"/></svg>
      <span>www.yourcbdnookplace.com</span>
    </div>
  </footer>
</main>
</body>
</html>
```